For Lease Sign to Attract National Retail Tenants

Attached is a logo design that was created by Pixel Harbor. I will like to develop a leasing sign that is 4 foot wide by 4 foot high or 4 feet wide and 6 feet high. I would like the sign to have a black background and use the colors that are in the logo. These will be signs that are placed in front of shopping centers and are often read by passing motorist so the sign must be simple, clean, very easy to read, distinctive, and have as few words as possible. It would be good if small amounts of bright green can be added as a boarder or ????? The text should be FOR LEASE, 555-283-7716, Wade Hollins. I will want to also design cards and letter head around the same theme.

Target Market(s)

National retail tenants wanting to lease space in my shopping centers

Industry/Entity Type

Real Estate Development

Contact Information for Business Card

Tern Holdings KR, LLC Wade Hollins President & CEO 4127 Orvell Ave. Suite 308 La Jolla, CA 92037 555-283-7716 wadehollins@mailvexa.example

```html
<!DOCTYPE html>
<html lang="en">
<head>
<meta charset="utf-8">
<title>Tern Holdings KR – Business Card</title>
<link rel="stylesheet" href="https://fonts.googleapis.com/css2?family=Libre+Baskerville:wght@700&family=Open+Sans:wght@400;600&display=swap">
<style>
  :root {
    --backdrop: #d9d9d9;
    --card-black: #050505;
    --card-white: #ffffff;
    --brand-red: #e0141b;
    --deep-red: #b3121a;
    --ink: #3a3a3a;
    --soft-grey: #c8c8c8;
    --logo-white: #f2f2f2;
  }
  * { box-sizing: border-box; margin: 0; padding: 0; }
  html, body { width: 1200px; height: 800px; overflow: hidden; }
  body {
    background: var(--backdrop);
    font-family: "Open Sans", Arial, sans-serif;
    display: flex;
    align-items: center;
    justify-content: center;
    gap: 40px;
  }
  .card {
    position: relative;
    width: 540px;
    height: 309px;
    overflow: hidden;
    box-shadow: 0 6px 18px rgba(0,0,0,0.18);
  }
  .card--front { background: var(--card-black); }
  .card--back { background: var(--card-white); }

  .edge-tab { position: absolute; width: 30px; height: 14px; }
  .edge-tab--top { top: 0; }
  .edge-tab--bottom { bottom: 0; }

  .front-brand {
    position: absolute;
    left: 0; right: 0; top: 112px;
    text-align: center;
  }
  .brand-name {
    font-family: "Open Sans", Arial, sans-serif;
    font-weight: 600;
    letter-spacing: 0.06em;
    white-space: nowrap;
  }
  .front-brand .brand-name {
    color: var(--logo-white);
    font-size: 26px;
    display: inline-flex;
    align-items: center;
    gap: 10px;
  }
  .brand-mark {
    display: inline-block;
    width: 12px; height: 12px;
    background: var(--brand-red);
  }
  .front-rule {
    width: 250px;
    height: 1px;
    background: var(--logo-white);
    margin: 12px auto 0;
  }
  .tagline {
    margin-top: 14px;
    color: var(--brand-red);
    font-size: 19px;
    letter-spacing: 0.04em;
  }
  .tagline .tagline-small { font-size: 14px; margin: 0 3px; }

  .back-brand {
    position: absolute;
    left: 34px; top: 186px;
  }
  .back-brand .brand-name {
    color: var(--brand-red);
    font-size: 17px;
    display: inline-flex;
    align-items: center;
    gap: 8px;
  }
  .contact-block {
    position: absolute;
    left: 300px; top: 54px;
    padding-left: 14px;
    border-left: 1px solid var(--soft-grey);
  }
  .contact-name {
    font-family: "Libre Baskerville", Georgia, serif;
    font-weight: 700;
    color: var(--deep-red);
    font-size: 18px;
    margin-bottom: 6px;
  }
  .contact-list { list-style: none; }
  .contact-item {
    display: flex;
    align-items: flex-start;
    gap: 6px;
    color: var(--ink);
    font-size: 11.5px;
    line-height: 17px;
    white-space: nowrap;
  }
  .contact-item svg { flex: none; margin-top: 4px; }
  .contact-item .indent { display: block; padding-left: 12px; }
</style>
</head>
<body>

  <section class="card card--front" aria-label="Business card front">
    <svg class="edge-tab edge-tab--top" style="left:255px" viewBox="0 0 30 14"><polygon points="0,0 30,0 24,14 6,14" fill="var(--brand-red)"/></svg>
    <div class="front-brand">
      <div class="brand-name"><span class="brand-mark"></span>TERN HOLDINGS KR, LLC</div>
      <div class="front-rule"></div>
      <p class="tagline">Contact<span class="tagline-small">for</span>LEASE</p>
    </div>
    <svg class="edge-tab edge-tab--bottom" style="left:330px" viewBox="0 0 30 14"><polygon points="6,0 24,0 30,14 0,14" fill="var(--brand-red)"/></svg>
  </section>

  <section class="card card--back" aria-label="Business card back">
    <svg class="edge-tab edge-tab--top" style="left:390px" viewBox="0 0 30 14"><polygon points="0,0 30,0 24,14 6,14" fill="var(--brand-red)"/></svg>

    <div class="back-brand">
      <div class="brand-name"><span class="brand-mark"></span>TERN HOLDINGS KR, LLC</div>
    </div>

    <div class="contact-block">
      <h2 class="contact-name">Wade Hollins</h2>
      <ul class="contact-list">
        <li class="contact-item">
          <svg width="8" height="9" viewBox="0 0 8 9"><path d="M4 0a3 3 0 0 1 3 3c0 2.2-3 6-3 6S1 5.2 1 3a3 3 0 0 1 3-3z" fill="var(--brand-red)"/><circle cx="4" cy="3" r="1" fill="#fff"/></svg>
          <span>000 Harlow Crest Rd., Unit 100,<span class="indent">Brenvale, XX 0000</span></span>
        </li>
        <li class="contact-item">
          <svg width="8" height="9" viewBox="0 0 8 9"><circle cx="4" cy="4.5" r="3.5" fill="none" stroke="var(--brand-red)" stroke-width="1"/><path d="M2.6 3c.4 1.4 1.1 2.1 2.4 2.6" stroke="var(--brand-red)" stroke-width="1.1" fill="none"/></svg>
          <span>555.283.7716</span>
        </li>
        <li class="contact-item">
          <svg width="8" height="9" viewBox="0 0 8 9"><circle cx="4" cy="4.5" r="3.5" fill="var(--brand-red)"/><rect x="2.2" y="3" width="3.6" height="3" fill="#fff"/></svg>
          <span>000.441.0000</span>
        </li>
        <li class="contact-item">
          <svg width="8" height="9" viewBox="0 0 8 9"><rect x="0.5" y="2" width="7" height="5" fill="none" stroke="var(--brand-red)"/><path d="M0.5 2l3.5 3 3.5-3" fill="none" stroke="var(--brand-red)"/></svg>
          <span>example@example.com</span>
        </li>
        <li class="contact-item">
          <svg width="8" height="9" viewBox="0 0 8 9"><circle cx="4" cy="4.5" r="3.5" fill="var(--brand-red)"/><path d="M4 2.5v4M2 4.5h4" stroke="#fff" stroke-width="1"/></svg>
          <span>www.example.com</span>
        </li>
      </ul>
    </div>

    <svg class="edge-tab edge-tab--bottom" style="left:180px" viewBox="0 0 30 14"><polygon points="6,0 24,0 30,14 0,14" fill="var(--brand-red)"/></svg>
  </section>

</body>
</html>
```